Redesign start page for existing online shop

We are selling building material (chimneys and flue pipes) as well as fireplaces (stoves). For this online shop we need a new start page. The domain is kaminwelt-versand.de. Here you can see the current design. We want a smoother design with just one banner in the middle instead of the three in the first row. The look has to be more professional and trustworthy. You can therefore play with the colors. We want to try some different orange instead of our yellow / orange color. A few more things: - The phone number has to be bigger and more highlighted - So the 5 advantages at the top should be shown in a different way - New design for the products below - New footer

Target Market(s)

Germany and other countries in Europe.

Industry/Entity Type

Home Builder

Number of Pages Required

1 page

Font styles to use
Other font styles liked:
• Please se the font on our current site.

Colors
f78f20
f68d4c

Requirements
Must have
• - Clear design - Trustworthy look - All elements Which are now shown shoulderstand be still there after redesigning -
Nice to have
• - See the Following sites to have a clou about our wishes: glutvia.de warmbrio.de

```html
<!DOCTYPE html>
<html lang="en">
<head>
<meta charset="utf-8">
<title>Kaminwelt Versand – Start page</title>
<link rel="stylesheet" href="https://fonts.googleapis.com/css2?family=Open+Sans:wght@400;600;700;800&family=Open+Sans+Condensed:wght@700&display=swap">
<style>
:root{
  --orange:#f78f20;
  --orange-soft:#f68d4c;
  --red:#e8443a;
  --dark:#2a3038;
  --darker:#1f242b;
  --text:#444b52;
  --muted:#7a8088;
  --line:#dcdcdc;
  --grey:#ececec;
  --grey-2:#f4f4f4;
  --white:#fff;
}
*{box-sizing:border-box;margin:0;padding:0}
html,body{width:1200px;height:3072px;overflow:hidden}
body{font-family:"Open Sans",Arial,sans-serif;color:var(--text);background:var(--white);position:relative;font-size:12px}
.abs{position:absolute}
.container{position:absolute;left:92px;width:1016px}

/* top bar */
.topbar{top:0;left:0;width:1200px;height:25px;border-bottom:1px solid var(--line);font-size:11px;color:var(--text)}
.topbar .usp{position:absolute;top:5px;display:flex;gap:6px;align-items:center}
.topbar .usp i{width:8px;height:8px;background:var(--dark);border-radius:50%;display:inline-block}
.topbar .usp.promo{color:var(--orange)}
.topbar .links{position:absolute;right:92px;top:5px}
.topbar .links span{padding:0 6px;border-left:1px solid var(--line)}
.topbar .links span:first-child{border:none}

/* header */
.header{top:25px;left:0;width:1200px;height:114px}
.logo{position:absolute;left:92px;top:32px;display:flex;align-items:center;gap:10px}
.logo .mark{width:42px;height:42px;border-radius:50%;background:var(--orange)}
.logo .name{font-weight:700;font-size:21px;line-height:21px;color:var(--dark);text-transform:uppercase}
.search{position:absolute;left:333px;top:38px;width:370px;height:40px;border:1px solid var(--line);border-radius:3px}
.search svg{position:absolute;right:12px;top:11px}
.badge{position:absolute;top:30px;width:46px;height:46px;border-radius:50%;background:#d9d9d9}
.badge.square{border-radius:4px;background:#e6e6e6;border:1px solid var(--line)}
.phone{position:absolute;right:92px;top:30px;text-align:right}
.phone .num{font-size:25px;font-weight:700;color:var(--red);display:flex;align-items:center;gap:8px}
.phone .hours{font-size:10px;color:var(--muted);margin-top:2px}

/* nav */
.nav{top:139px;left:0;width:1200px;height:45px;background:var(--dark);color:var(--white);font-size:12px}
.nav ul{list-style:none;position:absolute;left:92px;top:14px;display:flex;gap:26px}
.nav ul li::after{content:"";display:inline-block;margin-left:5px;border:solid var(--white);border-width:0 1.5px 1.5px 0;padding:2px;transform:rotate(45deg) translateY(-3px)}
.nav .right{position:absolute;right:92px;top:14px;display:flex;gap:24px;align-items:center}
.nav .advisor{color:var(--orange);font-weight:700}
.cart-dot{display:inline-block;width:14px;height:14px;border-radius:50%;background:var(--red);font-size:8px;text-align:center;line-height:14px;margin-left:4px}

/* hero */
.hero{top:184px;left:0;width:1200px;height:353px;background:linear-gradient(100deg,#2a4a8a 0%,#3b5ea6 28%,#c9c3b4 48%,#f3c21a 58%,#e7e2d8 68%,#3c5c9c 100%)}
.hero h1{position:absolute;left:127px;top:60px;font-family:"Open Sans Condensed","Open Sans",sans-serif;font-weight:700;color:var(--white);line-height:56px;font-size:56px;text-transform:uppercase;text-shadow:0 2px 6px rgba(0,0,0,.35)}
.hero h1 .thin{font-weight:400;font-family:"Open Sans",sans-serif;font-size:46px;letter-spacing:-1px}
.hero .cta{position:absolute;left:207px;top:250px;width:213px;height:51px;background:var(--orange);color:var(--dark);font-weight:700;font-size:11px;text-align:center;line-height:51px;border-radius:3px}
.contact-form{position:absolute;left:803px;top:0;width:397px;height:353px;background:rgba(31,36,43,.92);padding:22px 22px 0 22px}
.contact-form h2{color:var(--white);font-family:"Open Sans Condensed",sans-serif;font-size:28px;text-transform:uppercase;margin-bottom:14px}
.field{width:228px;height:38px;background:#f3f3f3;margin-left:17px;margin-bottom:10px;font-size:11px;color:var(--text);padding:10px}
.field.msg{height:82px}
.submit{width:228px;height:42px;background:var(--red);margin-left:17px;color:var(--white);font-weight:700;font-size:13px;text-align:center;line-height:42px}

/* brands */
.brands{top:537px;left:0;width:1200px;height:94px;border-bottom:1px solid var(--line)}
.brands .arrow{position:absolute;top:30px}
.brands .row{position:absolute;left:140px;top:30px;width:920px;display:flex;justify-content:space-between;align-items:center}
.brand{font-weight:700;font-size:20px;color:#8c9096}
.brand-sq{width:40px;height:32px;background:#c9ccd0}

/* orange strip */
.strip{top:631px;left:0;width:1200px;height:51px;background:var(--orange);color:var(--white);font-family:"Open Sans Condensed",sans-serif;font-size:17px;text-transform:uppercase}
.strip .item{position:absolute;top:15px;display:flex;align-items:center;gap:8px}
.strip .item i{width:16px;height:16px;border-radius:50%;background:var(--white)}
.strip .discover{position:absolute;right:92px;top:13px;color:var(--dark);font-size:21px}

/* features */
.features{top:682px;left:0;width:1200px;height:174px;background:var(--grey);display:flex}
.feature{flex:1;border-right:1px solid #d5d5d5;text-align:center;padding-top:28px;font-size:10px;font-weight:700;color:var(--dark);text-transform:uppercase;line-height:14px}
.feature:last-child{border:none}
.feature .ico{width:64px;height:64px;margin:0 auto 18px;border-radius:50%;border:2px solid #c8c8c8;background:var(--white);display:flex;align-items:center;justify-content:center}

/* products */
.products{top:915px;display:grid;grid-template-columns:repeat(4,231px);column-gap:30px;row-gap:27px}
.card{position:relative;height:330px;border:1px solid var(--line);background:var(--white);text-align:center}
.card .photo{height:152px;margin:20px 40px 12px;background:linear-gradient(180deg,#f4f4f4,#d6d8da);border-radius:2px}
.card h3{font-size:15px;font-weight:600;color:var(--orange-soft);line-height:18px;padding:0 12px}
.card p{font-size:11px;line-height:15px;color:var(--text);margin:8px 14px 0;height:30px;overflow:hidden}
.card .foot{position:absolute;left:0;bottom:0;width:100%;height:60px;background:var(--grey);display:flex;align-items:center;justify-content:space-between;padding:0 12px;font-size:11px;color:var(--dark)}
.card .btn{border:1px solid var(--orange-soft);color:var(--orange-soft);padding:7px 14px;font-size:11px;background:var(--white)}
.card.active{border-color:#9aa0a6;box-shadow:0 3px 10px rgba(0,0,0,.12)}
.card.active h3{color:var(--dark)}
.card.active .foot{background:var(--orange);color:var(--white)}
.card.active .btn{border-color:var(--white);color:var(--white);background:transparent}
.card .share{display:flex;justify-content:center;gap:8px;margin-top:12px}
.card .share i{width:18px;height:18px;border-radius:50%;border:1px solid #bbb}
.flag{position:absolute;right:-1px;top:-1px;width:32px;height:34px;background:var(--dark);color:var(--white);font-size:9px;font-weight:700;line-height:10px;padding-top:5px;clip-path:polygon(0 0,100% 0,100% 100%,50% 80%,0 100%)}
.heart{position:absolute;left:10px;top:8px}
.card.tall .photo{height:170px}

/* consultation */
.consult{top:1659px;left:0;width:1200px;height:405px;background:var(--grey)}
.consult h2{position:absolute;left:92px;top:64px;font-size:21px;font-weight:400;color:var(--dark);padding-bottom:10px;border-bottom:1px solid var(--orange)}
.consult .steps{position:absolute;left:92px;top:136px;display:flex;gap:40px;font-size:11px;font-weight:700;color:var(--dark)}
.consult .steps div{text-align:center}
.consult .steps svg{display:block;margin:0 auto 10px}
.consult .copy{position:absolute;left:92px;top:224px;width:480px;font-size:11px;line-height:17px}
.consult .btn{position:absolute;left:92px;top:308px;width:199px;height:39px;border:2px solid var(--dark);background:var(--white);font-size:11px;font-weight:700;text-align:center;line-height:35px;color:var(--dark)}
.mounting{position:absolute;left:637px;top:0;width:563px;height:405px;background:linear-gradient(160deg,#3e5c97,#2d3e60 60%,#4b5a6c);clip-path:polygon(8% 0,100% 0,100% 100%,0 100%)}
.mounting .gear{position:absolute;left:250px;top:70px}
.mounting h3{position:absolute;left:0;width:620px;text-align:center;top:190px;color:var(--white);font-size:19px;font-weight:700;text-transform:uppercase}
.mounting .sub{position:absolute;left:140px;width:340px;text-align:center;top:220px;color:#dfe4ee;font-size:11px;line-height:15px}
.mounting .price{position:absolute;left:156px;top:293px;width:128px;height:39px;background:var(--white);color:var(--dark);font-weight:700;font-size:11px;text-align:center;line-height:39px}
.mounting .save{position:absolute;left:284px;top:293px;width:178px;height:39px;background:var(--orange);color:var(--white);font-weight:700;font-size:11px;text-align:center;line-height:39px;text-transform:uppercase}

/* seo text */
.seo{top:2064px}
.seo h2{position:absolute;left:0;top:34px;width:960px;font-size:19px;font-weight:400;color:var(--orange-soft);line-height:26px;text-decoration:underline}
.seo .photo{position:absolute;left:2px;top:123px;width:402px;height:353px;border:6px solid var(--white);box-shadow:0 0 0 1px var(--line);background:linear-gradient(180deg,#3f7fd0 0%,#a9cdf0 40%,#b98555 55%,#8a5c36 80%,#5d7a3c 100%)}
.seo .photo .tag{position:absolute;left:8px;top:8px;width:30px;height:30px;border-radius:50%;background:var(--white)}
.seo .text{position:absolute;left:445px;top:110px;width:555px;height:370px;overflow:hidden;font-size:11px;line-height:17px;border-right:3px solid var(--line);padding-right:14px}
.seo .text a{color:var(--red);font-weight:700;text-decoration:none}
.seo .text p{margin-bottom:14px}
.seo .text strong{color:var(--dark)}

/* trust */
.trust{top:2591px;left:0;width:1200px;height:108px;background:var(--grey)}
.trust h2{position:absolute;left:92px;top:26px;font-size:22px;font-weight:400;color:var(--muted);line-height:26px;padding-right:28px;border-right:1px solid #ccc;height:56px}
.trust .seal{position:absolute;top:34px;width:44px;height:44px;border-radius:50%;background:#d0d0d0}
.trust .seal.gold{background:#d5a829}
.trust p{position:absolute;top:30px;font-size:10px;line-height:14px;width:300px}
.trust p.italic{font-style:italic;width:290px}

/* payment */
.payment{top:2699px;left:0;width:1200px;height:90px;background:var(--orange)}
.payment h2{position:absolute;left:92px;top:30px;color:var(--white);font-size:21px;font-weight:600}
.payment .cards{position:absolute;left:442px;top:26px;display:flex;gap:12px}
.payment .cards span{width:78px;height:44px;background:var(--white);border-radius:3px;font-size:10px;font-weight:700;color:var(--dark);text-align:center;line-height:44px}

/* footer */
.footer{top:2789px;left:0;width:1200px;height:283px;background:var(--dark);color:#b9bec4;font-size:10px;line-height:21px}
.footer h3{font-size:15px;font-weight:400;color:#c7ccd1;margin-bottom:16px}
.footer .col{position:absolute;top:42px}
.footer .links{display:grid;grid-template-columns:155px 150px}
.footer .social{display:flex;gap:6px;margin-top:8px}
.footer .social i{width:14px;height:14px;border:1px solid #8d939a;border-radius:2px}
.footer .copy{position:absolute;bottom:0;left:0;width:1200px;height:38px;background:var(--darker);text-align:center;line-height:38px;font-size:9px;color:#6f757c}
</style>
</head>
<body>

<div class="abs topbar">
  <div class="usp" style="left:92px"><i></i>In 5 Min Deal</div>
  <div class="usp" style="left:208px"><i></i>Leading Brands</div>
  <div class="usp promo" style="left:336px">‹ With us get promotion</div>
  <div class="links"><span>Jobs</span><span>Contact</span><span>Blog</span></div>
</div>

<header class="abs header">
  <div class="logo"><span class="mark"></span><span class="name">Kaminwelt<br>Versand</span></div>
  <div class="search"><svg width="16" height="16" viewBox="0 0 16 16"><circle cx="6.5" cy="6.5" r="5" fill="none" stroke="#222" stroke-width="2"/><line x1="10" y1="10" x2="15" y2="15" stroke="#222" stroke-width="2.4"/></svg></div>
  <div class="badge" style="left:741px"></div>
  <div class="badge square" style="left:791px"></div>
  <div class="phone">
    <div class="num"><svg width="20" height="20" viewBox="0 0 24 24"><path fill="#e8443a" d="M6.6 10.8a15 15 0 0 0 6.6 6.6l2.2-2.2c.3-.3.7-.4 1-.2 1.1.4 2.3.6 3.6.6.6 0 1 .4 1 1V20c0 .6-.4 1-1 1C10.6 21 3 13.4 3 4c0-.6.4-1 1-1h3.5c.6 0 1 .4 1 1 0 1.3.2 2.5.6 3.6.1.3 0 .7-.2 1z"/></svg>07321/448 210 0</div>
    <div class="hours">MON - FRI 9:00 TO 18:00</div>
  </div>
</header>

<nav class="abs nav">
  <ul><li>ONLINE SHOP</li><li>SERVICE</li><li>STANDORTE</li><li>FÜR HÄNDLER</li><li>INSTALLATEURE</li></ul>
  <div class="right"><span class="advisor">☎ Product Advisor</span><span>My Account</span><span>Cart<span class="cart-dot">0</span></span></div>
</nav>

<section class="abs hero" role="img" aria-label="Photo of a craftsman in a blue work jacket with yellow helmet, gloves and tool belt">
  <h1>In 5 Minutes<br><span class="thin">to heating</span><br>Supply</h1>
  <div class="cta">OTHER OFFER</div>
  <form class="contact-form">
    <h2>Get in touch with us</h2>
    <div class="field">Name</div>
    <div class="field">Email</div>
    <div class="field msg">Message</div>
    <div class="submit">SUBMIT</div>
  </form>
</section>

<section class="abs brands">
  <svg class="arrow" style="left:90px" width="14" height="40" viewBox="0 0 14 40"><polyline points="12,2 2,20 12,38" fill="none" stroke="#bbb" stroke-width="1.5"/></svg>
  <div class="row">
    <span class="brand">ferrovent</span><span class="brand-sq"></span><span class="brand">ferrovent</span><span class="brand">Kamrad</span>
    <span class="brand-sq"></span><span class="brand">ferrovent</span><span class="brand">Kamrad</span><span class="brand-sq"></span>
  </div>
  <svg class="arrow" style="left:1096px" width="14" height="40" viewBox="0 0 14 40"><polyline points="2,2 12,20 2,38" fill="none" stroke="#bbb" stroke-width="1.5"/></svg>
</section>

<section class="abs strip">
  <div class="item" style="left:92px"><i></i>Top Consulting</div>
  <div class="item" style="left:276px"><i></i>Best Price Guaranteed</div>
  <div class="item" style="left:492px"><i></i>Fast Delivery</div>
  <div class="discover">Discover Now »</div>
</section>

<section class="abs features">
  <div class="feature"><div class="ico"><svg width="30" height="30" viewBox="0 0 30 30"><circle cx="15" cy="12" r="8" fill="none" stroke="#f78f20" stroke-width="2"/><polyline points="10,19 8,28 15,25 22,28 20,19" fill="none" stroke="#f78f20" stroke-width="2"/></svg></div>German<br>brand quality</div>
  <div class="feature"><div class="ico"><svg width="30" height="30" viewBox="0 0 30 30"><path d="M15 3 L25 7 V15 C25 21 20 25 15 27 C10 25 5 21 5 15 V7 Z" fill="none" stroke="#f78f20" stroke-width="2"/><polyline points="10,15 14,19 20,11" fill="none" stroke="#f78f20" stroke-width="2"/></svg></div>25 year<br>warranty</div>
  <div class="feature"><div class="ico"><svg width="30" height="30" viewBox="0 0 30 30"><circle cx="16" cy="15" r="10" fill="none" stroke="#f78f20" stroke-width="2"/><polyline points="16,9 16,15 20,17" fill="none" stroke="#f78f20" stroke-width="2"/><line x1="2" y1="12" x2="7" y2="12" stroke="#f78f20" stroke-width="2"/><line x1="3" y1="18" x2="7" y2="18" stroke="#f78f20" stroke-width="2"/></svg></div>Fast<br>delivery</div>
  <div class="feature"><div class="ico"><svg width="30" height="30" viewBox="0 0 30 30"><rect x="4" y="6" width="18" height="12" rx="3" fill="none" stroke="#f78f20" stroke-width="2"/><path d="M10 18 V23 L15 18" fill="none" stroke="#f78f20" stroke-width="2"/><rect x="13" y="11" width="13" height="9" rx="3" fill="none" stroke="#f78f20" stroke-width="2"/></svg></div>Free<br>consultation</div>
  <div class="feature"><div class="ico"><svg width="30" height="30" viewBox="0 0 30 30"><path d="M8 16 L14 22 L24 10" fill="none" stroke="#f78f20" stroke-width="2"/><circle cx="15" cy="15" r="11" fill="none" stroke="#f78f20" stroke-width="2" stroke-dasharray="4 3"/></svg></div>Nationwide<br>installation service</div>
</section>

<section class="container products">
  <article class="card"><span class="flag">10%<br>off</span><div class="photo" role="img" aria-label="Stainless steel chimney extension pipe"></div><h3>Chimney Extension</h3><p>Fireplace extensions configurable produced made to measure</p><div class="foot"><span>ab € 63,00</span><span class="btn">Add To Cart</span></div></article>
  <article class="card active"><svg class="heart" width="14" height="13" viewBox="0 0 14 13"><path d="M7 12 C2 8 0 6 0 3.5 A3.5 3.5 0 0 1 7 2 A3.5 3.5 0 0 1 14 3.5 C14 6 12 8 7 12Z" fill="#f78f20"/></svg><span class="flag">8%<br>off</span><div class="photo" style="height:130px" role="img" aria-label="Metal chimney cover on four legs"></div><h3>Chimney Cover</h3><div class="share"><i></i><i></i><i></i><i></i><i></i></div><div class="foot"><span>ab € 63,00</span><span class="btn">Add To Cart</span></div></article>
  <article class="card"><div class="photo" role="img" aria-label="Insulated wall bushing block"></div><h3>Wall bushing</h3><p>Wall penetrations for the safe conduct of exhaust pipes through</p><div class="foot"><span>ab € 63,00</span><span class="btn">Add To Cart</span></div></article>
  <article class="card"><div class="photo" role="img" aria-label="Black angled stovepipe"></div><h3>Stovepipe</h3><p>Order stovepipes in black or gray cast in premium quality right here.</p><div class="foot"><span>ab € 63,00</span><span class="btn">Add To Cart</span></div></article>

  <article class="card"><div class="photo" role="img" aria-label="Lightweight chimney with red cap on stand"></div><h3>Lightweight Construction Chimney</h3><p>Lightweight construction chimneys are the perfect solution for an</p><div class="foot"><span>ab € 63,00</span><span class="btn">Add To Cart</span></div></article>
  <article class="card tall"><span class="flag">7%<br>off</span><div class="photo" role="img" aria-label="Stainless steel fireplace door"></div><h3>Fireplace Door</h3><p>Fireplace doors and flush doors made of stainless steel in</p><div class="foot"><span>ab € 63,00</span><span class="btn">Add To Cart</span></div></article>
  <article class="card tall"><div class="photo" role="img" aria-label="Black wood stove with burning fire"></div><h3>Stove</h3><p>Stoves with excellent price / performance ratio order free</p><div class="foot"><span>ab € 63,00</span><span class="btn">Add To Cart</span></div></article>
  <article class="card tall"><div class="photo" role="img" aria-label="Stainless steel chimney fan"></div><h3>Chimney Fans</h3><p>Chimney fans for the perfect train in the chimney.</p><div class="foot"><span>ab € 63,00</span><span class="btn">Add To Cart</span></div></article>
</section>

<section class="abs consult">
  <h2>Arrange An Appointment For Consultation</h2>
  <div class="steps">
    <div><svg width="22" height="22" viewBox="0 0 22 22"><rect x="2" y="4" width="18" height="16" fill="none" stroke="#f78f20" stroke-width="2"/><line x1="2" y1="9" x2="20" y2="9" stroke="#f78f20" stroke-width="2"/><line x1="7" y1="1" x2="7" y2="6" stroke="#f78f20" stroke-width="2"/><line x1="15" y1="1" x2="15" y2="6" stroke="#f78f20" stroke-width="2"/></svg>Recall the desired date</div>
    <div><svg width="22" height="22" viewBox="0 0 22 22"><circle cx="11" cy="11" r="9" fill="none" stroke="#f78f20" stroke-width="2"/><polyline points="11,6 11,11 14,13" fill="none" stroke="#f78f20" stroke-width="2"/></svg>Instant quotation</div>
    <div><svg width="22" height="22" viewBox="0 0 22 22"><polyline points="3,11 9,17 19,5" fill="none" stroke="#f78f20" stroke-width="3"/></svg>Real experts advice</div>
  </div>
  <p class="copy">Here you have the chance to comfortably arrange your call. At a given by you, you will then advise that you like about your chimney project a call by our experts. Please fill out the form below and specify the desired date for the recall.</p>
  <div class="btn">ADVICE HAVE AGREED &gt;&gt;</div>
  <div class="mounting" role="img" aria-label="Photo of an installer's blue work clothes with tool belt">
    <svg class="gear" width="80" height="80" viewBox="0 0 80 80"><circle cx="40" cy="40" r="14" fill="none" stroke="#fff" stroke-width="3"/><circle cx="40" cy="40" r="26" fill="none" stroke="#fff" stroke-width="3" stroke-dasharray="10 7"/></svg>
    <h3>Mounting Service</h3>
    <div class="sub">Nationwide steel chimney installation by professionals at an unbeatable fixed price</div>
    <div class="price">from € 599.00</div>
    <div class="save">Advantage price save</div>
  </div>
</section>

<section class="container seo">
  <h2>Stainless steel chimneys, chimney extensions, stovepipes and chimney accessories - at kaminwelt-versand.de buy</h2>
  <div class="photo" role="img" aria-label="House with wooden facade and stainless steel chimney under blue sky"><span class="tag"></span></div>
  <div class="text">
    <p>Can I use a <a>steel chimney</a> for sale on the Internet? This question you have probably never asked. For other products which is a matter of course, but with a stainless steel chimney you do not think first to the online shopping . There are the all around the subject for several years various platforms steel chimney offer. However, these providers operate their web shop only incidentally. This is reflected in the poor usability and the partly very outdated technology of pages. Kaminwelt Versand has gone a new way here. The goal was a pet shop for stainless steel chimneys and chimney accessories to put on their feet, which is composed not only professionally and according to the latest state of the art, but also gives you the security and usability that you are used to large online platforms in other sectors . With an efficient organization, modern technology and years of experience with the product steel chimney, this claim could be met. Best usability, certified privacy, quality products and expert advice by telephone round your shopping experience at Kaminwelt Versand.</p>
    <p><strong>Steel chimney, chimney kit and stainless steel chimney - all from one source.</strong></p>
    <p>Whether you have a double-walled stainless steel chimney , a chimney restoration looking for your old brick fireplace or chimney kit for your home: here you will find it. In our shop</p>
  </div>
</section>

<section class="abs trust">
  <h2>Shopping<br>Safely</h2>
  <div class="seal" style="left:258px"></div>
  <p style="left:352px">We offer exclusive products of German brand manufacturers. Our full range is manufactured from industry leaders and is subject to constant quality controls. For your safety, only the best for a fair price.</p>
  <div class="seal gold" style="left:757px"></div>
  <p class="italic" style="left:823px">To meet our premium quality and our service pledges, please contact us, of course, 25-year guarantee on all stainless steel chimneys and steel chimney components.</p>
</section>

<section class="abs payment">
  <h2>Payment Methods</h2>
  <div class="cards"><span>Kartiva</span><span>Novacard</span><span>Zahlwerk</span><span>Vorkasse</span><span>Bankeo</span><span>Trivant</span><span>Debitum</span></div>
</section>

<footer class="abs footer">
  <div class="col" style="left:92px"><h3>Quick Link</h3>
    <div class="links"><span>Frequently Asked</span><span>data protection</span><span>questions</span><span>imprint</span><span>about us</span><span>Contact us</span><span>Conditions</span><span>blog</span><span>revocation</span><span>glossary</span><span>delivery</span></div>
  </div>
  <div class="col" style="left:494px"><h3>Contact Us</h3>
    <div>Lindenweg 7<br>80331 Munich<br>Germany</div>
    <div style="margin-top:16px;line-height:16px">Kamin-Portal<br>Average rating: 4.71 (of 5). Calculated from<br>265 reviews.</div>
  </div>
  <div class="col" style="left:823px"><h3>Free Consultation</h3>
    <div style="line-height:16px">07321/448 210 0<br>Mo. Fr. 09:00 to 18:00<br>info@kaminwelt-versand.de</div>
    <div class="social"><i></i><i></i><i></i><i></i><i></i></div>
  </div>
  <div class="copy">© 2011 - 2016 Kaminwelt Versand</div>
</footer>

</body>
</html>
```